The Jawline Remedy Business Card

Looking for a business card design: front and back. It will be printed at pressquill.example on a leaf cutout tricolumn paper with green middle. 3.5 x 2 leaf cutout. It will need bleed room around edges. The front will have my picture, logo, website and email address. The back will be a quote. "Finally. The complete solution to helping you open your mouth fully without pain"
and
"Like Us on Chirpbook to Learn More @ The Jawline Remedy"

Target Market(s)

Women 20-55 years old

Industry/Entity Type

Health Service

Contact Information for Business Card

My photo on one side or embedded, Name: Dr. Marlow Keddick, PT, DPT, MS Website: TheJawlineRemedy.example Email: marlow@brightpathcareclinic.example

Requirements
Must have
• Unique design consistent with my logo

```html
<!DOCTYPE html>
<html lang="en">
<head>
<meta charset="utf-8">
<title>The Jawline Remedy – Business Card</title>
<link rel="stylesheet" href="https://fonts.googleapis.com/css2?family=Roboto:wght@400;500;700&display=swap">
<style>
  :root {
    --brand-blue: #1174bb;
    --brand-green: #8dc63f;
    --paper: #ffffff;
    --backdrop: #2b2b2b;
    --photo-light: #c9d3dc;
    --photo-dark: #6f7f8f;
  }
  * { box-sizing: border-box; margin: 0; padding: 0; }
  html, body { width: 1125px; height: 1200px; overflow: hidden; }
  body {
    background: var(--backdrop);
    font-family: "Roboto", Arial, sans-serif;
    position: relative;
  }
  .card {
    position: absolute;
    left: 166px;
    width: 798px;
    height: 454px;
    overflow: hidden;
  }
  .card--front {
    top: 104px;
    background: var(--paper);
    border-radius: 140px 0 140px 0;
  }
  .card--back {
    top: 620px;
    background: var(--brand-green);
    border-radius: 0 140px 0 140px;
    color: var(--paper);
  }
  .wave { position: absolute; inset: 0; width: 798px; height: 454px; }

  .brand {
    position: absolute;
    left: 68px;
    top: 72px;
    display: flex;
    align-items: center;
    gap: 22px;
  }
  .brand__mark {
    width: 150px; height: 150px;
    border: 7px solid var(--brand-blue);
    border-radius: 50%;
  }
  .brand__name {
    color: var(--brand-blue);
    font-weight: 700;
    font-size: 40px;
    line-height: 44px;
  }

  .portrait {
    position: absolute;
    left: 595px; top: 72px;
    width: 144px; height: 167px;
    border-radius: 16px;
    border: 2px solid var(--paper);
    background: linear-gradient(180deg, var(--photo-light), var(--photo-dark));
  }
  .identity {
    position: absolute;
    right: 59px; top: 252px;
    text-align: right;
    color: var(--paper);
  }
  .identity__name { font-weight: 700; font-size: 26px; line-height: 33px; }
  .identity__contact { margin-top: 12px; font-size: 17px; line-height: 23px; }

  .tagline {
    position: absolute;
    left: 51px; top: 131px;
    width: 190px;
    font-size: 18px;
    line-height: 23px;
  }
  .social {
    position: absolute;
    left: 51px; top: 251px;
  }
  .social__row { display: flex; align-items: center; gap: 8px; }
  .social__square { width: 44px; height: 44px; background: var(--paper); }
  .social__name { font-weight: 500; font-size: 20px; line-height: 23px; }
  .social__handle { font-size: 18px; line-height: 22px; margin-top: 4px; }
  .brand-circle {
    position: absolute;
    left: 404px; top: 60px;
    width: 360px; height: 360px;
    border-radius: 50%;
    background: var(--paper);
  }
</style>
</head>
<body>

<section class="card card--front" aria-label="Card front">
  <svg class="wave" viewBox="0 0 798 454" aria-hidden="true">
    <path d="M0,370 C120,425 250,405 350,315 C450,225 560,124 798,84 L798,454 L0,454 Z" fill="var(--brand-green)"/>
    <path d="M0,385 C120,440 260,420 360,330 C460,240 560,140 798,100 L798,454 L0,454 Z" fill="var(--paper)"/>
    <path d="M0,389 C120,444 264,424 364,334 C464,244 564,144 798,104 L798,454 L0,454 Z" fill="var(--brand-blue)"/>
  </svg>

  <div class="brand">
    <div class="brand__mark"></div>
    <div class="brand__name">The<br>Jawline<br>Remedy</div>
  </div>

  <div class="portrait" role="img" aria-label="Portrait photo of Dr. Marlow Keddick"></div>

  <div class="identity">
    <div class="identity__name">Dr. Marlow Keddick<br>PT, DPT, MS</div>
    <div class="identity__contact">
      555-014-2290<br>
      marlow@brightpathcareclinic.example<br>
      www.TheJawlineRemedy.example
    </div>
  </div>
</section>

<section class="card card--back" aria-label="Card back">
  <p class="tagline">Finally. The complete solution to helping you open your mouth fully without pain</p>
  <div class="social">
    <div class="social__row">
      <div class="social__square"></div>
      <div class="social__name">Like us on<br>Chirpbook</div>
    </div>
    <div class="social__handle">@ The Jawline Remedy</div>
  </div>
  <div class="brand-circle"></div>
</section>

</body>
</html>
```